Golden Crust Supper Invitation

We will be having a Fish Fry on May 17th from 6PM -10PM. Location is 4721 Quillon Ln. Mansfield, TX 76048. We need a Invitation, which includes a the header reading "Golden Crust Supper". Wording of "Golden Crust Supper" should incorporate both baseball and food batter. Think baseball bats dripping in batter. Admission to all you can eat fish fry will be a donation of any baseball equipment including: bats, gloves, jerseys, cleats, balls, or financial donation. Proceeds will go towards funding Pemberly Family in traveling to Dominican Republic to conduct baseball ministries. It would great to incorporate Dominican Republic flag or colors.

```html
<!DOCTYPE html>
<html lang="en">
<head>
<meta charset="utf-8">
<title>Golden Crust Supper Invitation</title>
<link rel="stylesheet" href="https://fonts.googleapis.com/css2?family=Alfa+Slab+One&family=Graduate&family=Poppins:wght@500;600&display=swap">
<style>
  :root {
    --backdrop: #d4d5d7;
    --paper: #fbf6ef;
    --navy: #0f1f5c;
    --red: #d42a3b;
    --gold: #eeab00;
    --white: #ffffff;
  }
  * { margin: 0; padding: 0; box-sizing: border-box; }
  html, body { width: 1110px; height: 1200px; overflow: hidden; background: var(--backdrop); }
  .invitation {
    position: absolute; left: 140px; top: 20px; width: 830px; height: 1160px;
    background: var(--paper); font-family: "Poppins", sans-serif; color: var(--navy);
  }
  .frame-outer { position: absolute; inset: 14px; border: 2px solid var(--red); border-radius: 12px; }
  .frame-inner { position: absolute; inset: 21px; border: 3px solid var(--navy); border-radius: 8px; }
  .header-art { position: absolute; left: 60px; top: 66px; width: 710px; height: 472px; border-radius: 60px;
    background: radial-gradient(ellipse at 50% 45%, #f7dd92, #f3c446 70%, #eeab00); }
  .ball { position: absolute; z-index: 2; top: 42px; width: 88px; height: 88px; border-radius: 50%;
    background: radial-gradient(circle at 40% 40%, #fffdf7, #efe6d3); border: 2px solid var(--navy); }
  .ball-left { left: 34px; } .ball-right { left: 705px; }
  .title { position: absolute; left: 60px; top: 200px; width: 710px; text-align: center;
    font-family: "Alfa Slab One", serif; font-size: 80px; line-height: 1.1; color: var(--navy); text-transform: uppercase; }
  .tagline-band { position: absolute; left: 72px; top: 608px; width: 685px; height: 51px; background: var(--gold);
    color: var(--white); font-family: "Graduate", serif; font-size: 30px; line-height: 51px; text-align: center;
    -webkit-text-stroke: 1px var(--white); }
  .date { position: absolute; left: 72px; top: 690px; overflow: visible; }
  .date-divider { position: absolute; left: 226px; top: 701px; width: 1px; height: 132px; background: var(--red); }
  .time { position: absolute; left: 239px; top: 690px; overflow: visible; }
  .time-rule { position: absolute; left: 239px; top: 794px; width: 518px; height: 1px; background: var(--red); }
  .address { position: absolute; left: 239px; top: 806px; overflow: visible; }
  .slab-text { font-family: "Alfa Slab One", serif; fill: var(--navy); }
  .varsity-text { font-family: "Graduate", serif; fill: var(--navy); stroke: var(--navy); stroke-width: 0.8; }
  .admission { position: absolute; left: 72px; top: 902px; width: 685px; height: 102px;
    border: 2px dashed var(--red); text-align: center; padding-top: 10px; }
  .admission-title { font-weight: 600; font-size: 23px; line-height: 26px; }
  .admission-text { font-weight: 500; font-size: 19px; line-height: 25px; }
  .ticket-icon { position: absolute; left: 80px; top: 872px; }
  .proceeds-row { position: absolute; left: 70px; top: 1034px; width: 690px; height: 58px; }
  .flag { position: absolute; top: 0; }
  .flag-left { left: 0; } .flag-right { left: 597px; }
  .proceeds { position: absolute; left: 99px; top: 0; width: 490px; height: 58px; background: var(--red);
    color: var(--white); font-weight: 500; font-size: 16.5px; line-height: 21px; text-align: center; padding-top: 8px; }
</style>
</head>
<body>
<main class="invitation">
  <div class="frame-outer"></div>
  <div class="frame-inner"></div>
  <div class="header-art" role="img" aria-label="Crossed baseball bats dripping with golden fry batter and a fried fish"></div>
  <div class="ball ball-left" role="img" aria-label="Baseball illustration"></div>
  <div class="ball ball-right" role="img" aria-label="Baseball illustration"></div>
  <h1 class="title">Golden Crust<br>Supper</h1>

  <p class="tagline-band">JOIN US FOR A COMMUNITY FISH FRY!</p>

  <svg class="date" width="145" height="150" viewBox="0 0 145 150">
    <text class="slab-text" x="0" y="67" font-size="76" textLength="143" lengthAdjust="spacingAndGlyphs">MAY</text>
    <text class="slab-text" x="0" y="144" font-size="76" textLength="143" lengthAdjust="spacingAndGlyphs">17TH</text>
  </svg>
  <div class="date-divider"></div>
  <svg class="time" width="520" height="100" viewBox="0 0 520 100">
    <text class="slab-text" x="0" y="86" font-size="102" textLength="192" lengthAdjust="spacingAndGlyphs">6PM</text>
    <rect x="227" y="45" width="31" height="4" fill="#0f1f5c"/>
    <text class="slab-text" x="286" y="86" font-size="102" textLength="233" lengthAdjust="spacingAndGlyphs">10PM</text>
  </svg>
  <div class="time-rule"></div>
  <svg class="address" width="525" height="32" viewBox="0 0 525 32">
    <text class="varsity-text" x="1" y="28" font-size="27" textLength="522" lengthAdjust="spacingAndGlyphs">4721 QUILLON LN. MANSFIELD, TX 76048</text>
  </svg>

  <svg class="ticket-icon" width="60" height="60" viewBox="0 0 60 60" aria-hidden="true">
    <g transform="rotate(-45 30 30)">
      <path d="M4 20 H56 V26 A4 4 0 0 0 56 34 V40 H4 V34 A4 4 0 0 0 4 26 Z" fill="#d42a3b"/>
      <line x1="44" y1="22" x2="44" y2="38" stroke="#fbf6ef" stroke-width="1.5" stroke-dasharray="2 2"/>
    </g>
  </svg>
  <section class="admission">
    <h2 class="admission-title">Admission:</h2>
    <p class="admission-text">Bring a donation of baseball equipment (bats, gloves,<br>jerseys, cleats, balls) or make a financial donation.</p>
  </section>

  <div class="proceeds-row">
    <svg class="flag flag-left" width="93" height="58" viewBox="0 0 93 58" aria-label="Dominican Republic flag" role="img">
      <rect width="93" height="58" fill="#ffffff"/>
      <rect x="0" y="0" width="41" height="24" fill="#0f1f5c"/>
      <rect x="52" y="0" width="41" height="24" fill="#d42a3b"/>
      <rect x="0" y="34" width="41" height="24" fill="#d42a3b"/>
      <rect x="52" y="34" width="41" height="24" fill="#0f1f5c"/>
    </svg>
    <p class="proceeds">Proceeds go toward helping the Pemberly Family travel<br>to the Dominican Republic for baseball ministries.</p>
    <svg class="flag flag-right" width="93" height="58" viewBox="0 0 93 58" aria-label="Dominican Republic flag" role="img">
      <rect width="93" height="58" fill="#ffffff"/>
      <rect x="0" y="0" width="41" height="24" fill="#0f1f5c"/>
      <rect x="52" y="0" width="41" height="24" fill="#d42a3b"/>
      <rect x="0" y="34" width="41" height="24" fill="#d42a3b"/>
      <rect x="52" y="34" width="41" height="24" fill="#0f1f5c"/>
    </svg>
  </div>
</main>
</body>
</html>
```